New Basketball Sports Agency need webpage design

We are a ZEMO/KXV Sports agency looking for a new Webpage design. We currently have a site @ www.pvtcourtwork.com, and looking for someone to redesign the site.. We are also looking to redo the LOGO as well. PVT will begin its Brightrun camps also, and would like a page to promote and sign up for camp. I already have tallywise, but not sure how to add to site. Site must include:

Page for Agency updates, Client profiles, page for admin, camp registration page, flash photos, and able to filter news updates from gryphonwire, and TRKO sites.

Target Market(s)

European basketball clubs, USA Teams, Basketball Players, Sports Agents, Sports Directors General Managers,

Industry/Entity Type

News

```html
<!DOCTYPE html>
<html lang="en">
<head>
<meta charset="utf-8">
<title>PVT Sports Management</title>
<link href="https://fonts.googleapis.com/css2?family=Fjalla+One&family=Source+Sans+3:wght@400;600&display=swap" rel="stylesheet">
<style>
:root{
  --bg:#050505;
  --panel:#141414;
  --panel-2:#1d1d1f;
  --text:#f2f2f2;
  --muted:#bdbdbd;
  --dim:#8a8a8a;
  --heading:#e6e6e6;
  --button:#4a5060;
  --gold:#c9a94a;
  --accent-red:#c0282a;
}
*{margin:0;padding:0;box-sizing:border-box}
html,body{width:964px;height:1200px;overflow:hidden;background:var(--bg)}
body{position:relative;font-family:"Source Sans 3",sans-serif;color:var(--text)}
.abs{position:absolute}

.header-photo{left:351px;top:0;width:613px;height:520px;background:radial-gradient(ellipse at 80% 20%,#5a4a3c 0%,#2a221c 35%,#0a0a0a 75%)}
.world-map{left:130px;top:0;width:230px;height:125px;background:radial-gradient(ellipse at 50% 40%,#6d6450 0%,#2b271e 60%,transparent 100%);opacity:.8}
.brand{left:88px;top:6px;width:180px;height:90px;display:flex;align-items:center;gap:8px}
.brand-mark{width:22px;height:22px;border-radius:50%;background:var(--gold)}
.brand-name{font-family:"Fjalla One",sans-serif;font-size:46px;color:var(--gold);letter-spacing:1px}
.tagline{left:88px;top:96px;font-family:"Fjalla One",sans-serif;font-size:22px;letter-spacing:4px;color:#9d9d9d}

.nav{left:351px;top:82px;width:530px;height:56px;background:rgba(40,40,42,.85);display:flex;align-items:center;justify-content:space-around;padding:0 10px}
.nav a{font-family:"Fjalla One",sans-serif;font-size:15px;color:#fff;text-decoration:none;letter-spacing:.3px}

.hero{left:83px;top:139px;width:798px;height:371px;background:linear-gradient(100deg,#3c3f46 0%,#5a4535 45%,#2d2f35 100%)}
.hero-arrows{left:791px;top:414px}

.welcome{left:92px;top:532px;font-size:21px;font-weight:400;color:var(--heading);letter-spacing:.3px}
.video{left:94px;top:573px;width:284px;height:194px;background:#2a2a2a;padding:6px}
.video-frame{width:100%;height:100%;background:linear-gradient(160deg,#3a2e2a,#15151a 70%);position:relative}
.intro-title{left:398px;top:577px;font-size:14.5px;color:#fff}
.intro-body{left:398px;top:601px;width:470px;font-size:11px;line-height:19.3px;color:#dcdcdc}
.btn{display:inline-block;background:var(--button);color:#fff;font-size:12px;text-align:center;border-radius:3px}
.btn-intro{left:395px;top:736px;width:84px;height:27px;line-height:27px}

.col-title{top:788px;font-size:18px;color:#fff}
.news-photo{left:93px;top:835px;width:222px;height:83px;border:3px solid #e8e8e8;border-radius:4px;background:linear-gradient(90deg,#b8a78a,#8d7c9e)}
.news-title{left:95px;top:926px;width:230px;font-size:12.5px;line-height:16px;color:#fff}
.news-body{left:95px;top:964px;width:230px;font-size:10px;line-height:16px;color:var(--muted)}
.btn-news{left:95px;top:1025px;width:84px;height:27px;line-height:27px}

.awards{left:365px;top:832px;list-style:none}
.awards li{font-size:10px;line-height:29px;color:#fff;display:flex;align-items:center;gap:7px}
.awards li::before{content:"";border-left:6px solid #fff;border-top:5px solid transparent;border-bottom:5px solid transparent}

.pager{top:796px}

.link-card{left:636px;width:218px;height:70px;background:var(--panel-2);display:flex;align-items:center;padding:0 10px;gap:12px}
.link-badge{width:32px;height:46px;background:#5b6478;border-radius:2px;flex:none}
.link-kind{font-family:"Fjalla One",sans-serif;font-size:13px;color:#b7b7c3;letter-spacing:.3px}
.link-name{font-size:14.5px;color:#fff;line-height:19px}
.link-desc{font-size:9.5px;color:#cfcfcf}

.footer{left:170px;top:1080px;width:794px;height:120px;background:linear-gradient(90deg,#0b0b0b,#1c1c1c 40%,#121212)}
.footer-links{left:99px;top:1113px;font-size:12.5px;color:#e8e8e8}
.footer-links span{color:#aaa;margin:0 5px}
.copyright{left:99px;top:1140px;font-size:9.5px;color:var(--dim)}
.social{left:723px;top:1108px;display:flex;gap:2px}
.social-dot{width:27px;height:27px;border-radius:50%;display:flex;align-items:center;justify-content:center;font-size:7px;font-weight:600;color:#fff}
</style>
</head>
<body>
<div class="abs header-photo" role="img" aria-label="Dark photo of a basketball player's shoulder and face"></div>
<div class="abs world-map" role="img" aria-label="Faint gold world map behind the logo"></div>
<div class="abs brand"><span class="brand-mark"></span><span class="brand-name">PVT</span></div>
<div class="abs tagline">WORLD WIDE</div>

<nav class="abs nav">
  <a href="#">HOME</a><a href="#">CLIENTS</a><a href="#">BASKETBALL BOOTCAMP</a><a href="#">HIGH SCHOOL SERVICES</a><a href="#">MORE</a>
</nav>

<div class="abs hero" role="img" aria-label="Studio photo of an athlete holding a basketball on his shoulder"></div>
<svg class="abs hero-arrows" width="60" height="54" viewBox="0 0 60 54">
  <polyline points="22,2 4,27 22,52" fill="none" stroke="#6b6b6b" stroke-width="4"/>
  <polyline points="38,2 56,27 38,52" fill="none" stroke="#d0d0d0" stroke-width="4"/>
</svg>

<h1 class="abs welcome">WELCOME TO PIVOT SPORTS MANAGEMENT</h1>

<div class="abs video">
  <div class="video-frame" role="img" aria-label="Video still of a player shooting in a game">
    <svg width="272" height="182" viewBox="0 0 272 182" style="position:absolute;left:0;top:0">
      <circle cx="136" cy="88" r="20" fill="#e6e6e6"/>
      <polygon points="130,78 130,98 145,88" fill="#222"/>
      <rect x="0" y="156" width="272" height="26" fill="#1a1a1a"/>
      <rect x="0" y="156" width="272" height="3" fill="#555"/>
      <rect x="0" y="156" width="93" height="3" fill="var(--accent-red)"/>
      <circle cx="93" cy="157" r="4" fill="#ccc"/>
      <rect x="16" y="165" width="2" height="8" fill="#ccc"/><rect x="21" y="165" width="2" height="8" fill="#ccc"/>
      <polygon points="42,167 46,167 50,163 50,175 46,171 42,171" fill="#ccc"/>
      <text x="62" y="173" font-size="7" fill="#bbb" font-family="sans-serif">0:02 / 0:10</text>
      <text x="212" y="173" font-size="7" fill="#bbb" font-family="sans-serif">720p</text>
      <rect x="237" y="165" width="8" height="7" fill="none" stroke="#bbb"/>
      <rect x="254" y="164" width="9" height="9" fill="none" stroke="#bbb" stroke-dasharray="3 3"/>
    </svg>
  </div>
</div>

<p class="abs intro-title">Etiam est nunc, venenatis in, tristique eu, imperdiet ac, nisl.</p>
<p class="abs intro-body">Cum sociis natoque penatibus et magnis dis parturient montes, nascetur ridiculus mus. In iaculis facilisis massa. Etiam eu urna. Sed porta. Suspendisse quam leo, molestie sed, luctus quis, feugiat in, pede. Fusce tellus. Sed metus augue, convallis et, vehicula ut, pulvinar eu, ante. Nunc tempus felis vitae urna. Vivamus porttitor, g, purus nisi eleifend libero, a tempus libero Sed ut perspiciatis unde omnis iste natus error sit voluptatem accusantium doloremque laudantium, totam rem aperiam, eaque ipsa quae ab illo inventore veritatis</p>
<a class="abs btn btn-intro">VIEW MORE</a>

<h2 class="abs col-title" style="left:95px">Latest News</h2>
<div class="abs news-photo" role="img" aria-label="Portrait of the signed point guard beside his college team name"></div>
<p class="abs news-title">PVT signs Brookvale's Point Guard Darnell Whitcomb</p>
<p class="abs news-body">Darnell is a floor general with tremendous heart and determination···Will battle tooth and nail on every possession···Clutch performer who</p>
<a class="abs btn btn-news">VIEW MORE</a>

<h2 class="abs col-title" style="left:365px">Awards/Achievements</h2>
<svg class="abs pager" style="left:568px" width="16" height="10" viewBox="0 0 16 10"><polygon points="6,0 0,5 6,10" fill="#999"/><polygon points="10,0 16,5 10,10" fill="#999"/></svg>
<ul class="abs awards">
  <li>2010-All Confrence Freshman Team(Coastline)</li>
  <li>2013-NCCB Mid-East Region 1st Team</li>
  <li>2013-All Mid-East Region 1st Team</li>
  <li>2013-R-VAC Athlete of the Week (2X)</li>
  <li>2013-Ranked R-VAC Top 5-Steels (#1)</li>
  <li>2013-Ranked R-VAC Top 10-Rebound (#8)</li>
  <li>2013-Ranked R-VAC Top 5-Scoring (#5)</li>
  <li>2013-Ranked R-VAC Top 5-Assists(#3)</li>
</ul>

<h2 class="abs col-title" style="left:636px">Links &amp; Resources</h2>
<svg class="abs pager" style="left:830px" width="16" height="10" viewBox="0 0 16 10"><polygon points="6,0 0,5 6,10" fill="#999"/><polygon points="10,0 16,5 10,10" fill="#999"/></svg>

<div class="abs link-card" style="top:827px"><span class="link-badge"></span><div><div class="link-kind">PRO BASKETBALL</div><div class="link-name">KXV</div><div class="link-desc">League, Team, Player info...</div></div></div>
<div class="abs link-card" style="top:902px"><span class="link-badge"></span><div><div class="link-kind">NCCL BASKETBALL</div><div class="link-name">NCCL</div><div class="link-desc">Eligibility, Academics, Resources</div></div></div>
<div class="abs link-card" style="top:978px"><span class="link-badge"></span><div><div class="link-kind">MISC BASKETBALL</div><div class="link-name">CourtLine</div><div class="link-desc">Eligibility, Guide for Youth Bas-</div></div></div>

<div class="abs footer"></div>
<nav class="abs footer-links">Home<span>|</span>Clients<span>|</span>Basketball Bootcamp<span>|</span>High School Services<span>|</span>Links</nav>
<p class="abs copyright">© 2013 Company Name.&nbsp; All right reserved.&nbsp; Term of Use</p>
<div class="abs social">
  <span class="social-dot" style="background:#3b5a9a">FN</span>
  <span class="social-dot" style="background:#3aa3dc">CL</span>
  <span class="social-dot" style="background:#2f8bc0">WW</span>
  <span class="social-dot" style="background:#f07a1c">RSS</span>
</div>
</body>
</html>
```